UI/UX design for non-profit education/student success foundation website

Looking to work with a ui/ux designer that can provide an elegant, impactful and modern responsive design for a non-profit education/student success foundation website. The website will need to have a lot of visuals and elements with impactful statements. The responsive templates will later be parsed (this will be done by another developer) and converted to Concrete5 CMS templates. The organization likes bold colors with a modern sleek design. Typography is also key in titles and statements of interest. On-scroll visuals could be nice if it lends well to combining imagery and text. The site will need templates for a homepage, global sub-page, and contact page. Interchangeable block elements would be nice if we want to create other templates or change element positions.

Target Market(s)

Continued education and philanthropy individuals/organizations

Industry/Entity Type

Non-profit / college education

Coding

Coded - Design and coding required

Number of Pages Required

3 page

Font styles to use
Sans Serif
Script

Colors
0094D4
00A9DD
6FCCEA
C7EBF8
E9F6FB
59FF00
82FF00
B8FF75
E3FFCB
F4FFEA
FFC000
F8CF3A
FAE287
FDF2CF
FEFAEE
EE7325
F08F49
F5BC92
FAE3D3
FDF4ED
6B429C
8869AF
B7A5CE
E3DAEB
F3F0F8

Requirements
Must have
• Modern responsive design, impactful visual elements, available theme elements pre styled for things like forms, buttoms, tables...
Nice to have
• Onscroll vidual effects, heros with background video

```html
<!DOCTYPE html>
<html lang="en">
<head>
<meta charset="utf-8">
<title>Northway Foundation</title>
<link href="https://fonts.googleapis.com/css2?family=Montserrat:wght@600;700&family=Roboto:wght@400;500;700&display=swap" rel="stylesheet">
<style>
:root{
  --orange:#ee7325;
  --ink:#222222;
  --text:#555555;
  --dark:#262626;
  --white:#ffffff;
  --line:#e4e4e4;
}
*{box-sizing:border-box;margin:0;padding:0}
html,body{width:1200px;height:4007px;overflow:hidden}
body{font-family:'Roboto',sans-serif;color:var(--ink);background:var(--white);position:relative}
.abs{position:absolute}
h1,h2,h3,.brand{font-family:'Montserrat',sans-serif;font-weight:700}
.accent{color:var(--orange)}
.btn{position:absolute;background:var(--orange);color:var(--white);font-family:'Roboto',sans-serif;font-weight:700;font-size:15px;text-transform:uppercase;display:flex;align-items:center;justify-content:center;gap:12px}
.para{font-size:13px;line-height:25px;color:var(--text);text-align:justify}

/* header */
.topline{position:absolute;top:0;left:0;width:1200px;height:5px;background:var(--orange)}
.brand{font-size:26px;color:var(--ink);letter-spacing:.3px;white-space:nowrap}
.contact-item{position:absolute;top:20px;display:flex;align-items:center;gap:20px}
.contact-item .circle{width:50px;height:50px;border-radius:50%;background:var(--orange);display:flex;align-items:center;justify-content:center}
.contact-item .label{font-size:14px;font-weight:700;text-transform:uppercase;color:var(--ink)}
.contact-item .value{font-size:19px;font-weight:500;color:var(--orange);margin-top:3px;white-space:nowrap}
.navbar{position:absolute;left:112px;top:84px;width:976px;height:50px;background:var(--dark);z-index:2;display:flex;align-items:center}
.navbar a{color:var(--white);font-size:14.5px;font-weight:500;text-decoration:none;margin-left:16px;margin-right:6px}
.navbar .donate{position:absolute;right:0;top:0;height:50px;width:133px;background:var(--orange);display:flex;align-items:center;justify-content:center;margin:0;font-weight:700}

/* hero */
.hero{position:absolute;left:0;top:107px;width:1200px;height:601px;background:linear-gradient(100deg,#3c2f26 0%,#6b5443 35%,#8a7866 60%,#b7b6b0 100%)}
.hero h1{position:absolute;left:112px;top:218px;font-size:35px;line-height:44px;color:var(--white);text-transform:uppercase}
.dots{position:absolute;left:112px;top:573px;display:flex;gap:8px}
.dots span{width:12px;height:12px;border:2px solid var(--white);background:transparent}
.dots span.on{background:var(--orange)}

/* sections */
.section-title{font-size:35px;text-transform:uppercase}
.photo{position:absolute}
.services{position:absolute;left:0;top:1285px;width:1200px;height:595px;background:linear-gradient(90deg,#2d2a26 0%,#4a4036 45%,#3a3630 100%)}
.services h2{position:absolute;width:100%;text-align:center;top:55px;font-size:35px;color:var(--white)}
.services .intro{position:absolute;left:160px;width:880px;top:114px;text-align:center;font-size:15px;line-height:25px;color:var(--white)}
.service{position:absolute;top:222px;width:305px;color:var(--white)}
.service h3{font-family:'Roboto',sans-serif;font-size:18.5px;font-weight:500;margin-top:12px;text-transform:uppercase}
.service p{font-size:13.5px;line-height:23px;margin-top:18px;text-align:justify}

.blog{position:absolute;left:0;top:2457px;width:1200px;height:599px;background:var(--orange)}
.blog h2{position:absolute;width:100%;text-align:center;top:44px;font-size:35px;color:var(--white)}
.card{position:absolute;background:var(--white)}
.date{display:inline-block;border:1px solid var(--line);color:var(--orange);font-size:12px;font-weight:500;padding:5px 12px;background:var(--white)}
.card h3{font-family:'Roboto',sans-serif;font-weight:500;font-size:16.5px;line-height:27px;text-transform:uppercase;color:var(--ink)}
.card p{font-size:14px;line-height:22px;color:var(--text)}

.field{position:absolute;background:var(--white);border:1px solid #ececec;box-shadow:0 1px 4px rgba(0,0,0,.08);font-size:14.5px;color:#555;padding:17px 16px}

.footer{position:absolute;left:0;top:3674px;width:1200px;height:333px;background:var(--dark);color:var(--white)}
.footer .brand{color:var(--white);position:absolute;width:100%;text-align:center;top:38px}
.footnav{position:absolute;width:100%;top:92px;display:flex;justify-content:center;gap:25px;font-size:15.5px;font-weight:500}
.footcontact{position:absolute;width:100%;top:133px;display:flex;justify-content:center;align-items:center;gap:14px;font-size:17px;font-weight:500}
.footer .rule{position:absolute;left:112px;width:976px;top:267px;height:1px;background:#555}
.copy{position:absolute;width:100%;top:290px;text-align:center;font-size:12px}
</style>
</head>
<body>

<div class="topline"></div>
<header>
  <div class="abs brand" style="left:111px;top:28px">NORTHWAY FOUNDATION</div>
  <div class="contact-item" style="left:556px">
    <div class="circle">
      <svg width="22" height="16" viewBox="0 0 22 16"><rect x="1" y="1" width="20" height="14" rx="2" fill="#fff"/><path d="M2 2 L11 9 L20 2" stroke="#ee7325" stroke-width="2" fill="none"/></svg>
    </div>
    <div><div class="label">Email us:</div><div class="value">info@northway.org</div></div>
  </div>
  <div class="contact-item" style="left:888px">
    <div class="circle">
      <svg width="22" height="22" viewBox="0 0 24 24"><path fill="#fff" d="M6.6 10.8c1.4 2.8 3.8 5.1 6.6 6.6l2.2-2.2c.3-.3.7-.4 1-.2 1.1.4 2.3.6 3.6.6.6 0 1 .4 1 1V20c0 .6-.4 1-1 1C10.6 21 3 13.4 3 4c0-.6.4-1 1-1h3.5c.6 0 1 .4 1 1 0 1.3.2 2.5.6 3.6.1.3 0 .7-.2 1z"/></svg>
    </div>
    <div><div class="label">Call us:</div><div class="value">555-010-2040</div></div>
  </div>
  <nav class="navbar">
    <a>HOME</a><a>ABOUT US</a><a>OUR SERVICES</a><a>WHY CHOOSE US</a><a>BLOG</a><a>CONTACT US</a>
    <a class="donate">DONATE NOW</a>
  </nav>
</header>

<section class="hero" role="img" aria-label="Smiling student with glasses holding a pen in a library">
  <h1>Welcome to Northway<br>Foundation</h1>
  <div class="btn" style="left:112px;top:335px;width:142px;height:48px">Get Started</div>
  <div class="dots"><span></span><span class="on"></span><span></span><span></span></div>
</section>

<section class="about">
  <div class="photo" role="img" aria-label="Three students studying together with a laptop and book" style="left:0;top:804px;width:600px;height:386px;background:linear-gradient(120deg,#d9b48a 0%,#b6845c 40%,#8a6a55 70%,#a9b8b6 100%)"></div>
  <h2 class="abs section-title" style="left:663px;top:830px">About <span class="accent">Us</span></h2>
  <p class="abs para" style="left:663px;top:897px;width:426px">The Northway Foundation was founded from Martin and Helen Greaves’ vision to design an innovative program that would dramatically increase the graduation rates of first-generation college students—those who are first in their family to attend college. For several years prior to starting the foundation, the Greaves endowed scholarships at Ridgeview State University (RSU) and Northfield College (NFC) in order to help students</p>
  <div class="btn" style="left:663px;top:1105px;width:142px;height:51px">Learn More</div>
</section>

<section class="services" role="img" aria-label="Dimmed photo of a student smiling at a laptop">
  <h2>OUR SERVICES</h2>
  <p class="intro">Lorem ipsum dolor sit amet, consectetur adipiscing elit, sed do eiusmod tempor incididunt ut labore et dolore magna aliqua ut enim ad minim venscing elit, sed do eiusmod tempor iiam, quis nostrud.</p>
  <div class="service" style="left:112px">
    <svg width="56" height="56" viewBox="0 0 56 56" fill="none" stroke="#ee7325" stroke-width="2"><rect x="3" y="6" width="50" height="34" rx="2"/><circle cx="28" cy="20" r="6"/><path d="M17 38c2-7 6-10 11-10s9 3 11 10"/><circle cx="10" cy="14" r="4"/><circle cx="46" cy="14" r="4"/><path d="M20 46h16M28 40v12"/></svg>
    <h3>Thought-Leadership</h3>
    <p>Lorem ipsum dolor sit amet, consectetur adipiscing elit, sed do eiusmod tempor incididunt ut labore et dolore magna aliqua ut enim ad minim veniam quis nostrud.</p>
  </div>
  <div class="service" style="left:448px">
    <svg width="56" height="56" viewBox="0 0 56 56" fill="none" stroke="#ee7325" stroke-width="2"><path d="M17 5h22v14c0 7-5 12-11 12s-11-5-11-12z"/><path d="M17 9H9c0 7 3 11 8 11M39 9h8c0 7-3 11-8 11"/><path d="M28 31v9M20 40h16v6H20zM16 46h24v5H16z"/></svg>
    <h3>Scholarships</h3>
    <p>Lorem ipsum dolor sit amet, consectetur adipiscing elit, sed do eiusmod tempor incididunt ut labore et dolore magna aliqua ut enim ad minim veniam quis nostrud.</p>
  </div>
  <div class="service" style="left:784px">
    <svg width="56" height="56" viewBox="0 0 56 56" fill="none" stroke="#ee7325" stroke-width="2"><circle cx="28" cy="12" r="6"/><path d="M18 30c1-7 5-10 10-10s9 3 10 10"/><circle cx="12" cy="24" r="4"/><circle cx="44" cy="24" r="4"/><rect x="6" y="34" width="44" height="16"/><rect x="38" y="4" width="14" height="9" rx="2"/></svg>
    <h3>Speaking</h3>
    <p>Lorem ipsum dolor sit amet, consectetur adipiscing elit, sed do eiusmod tempor incididunt ut labore et dolore magna aliqua ut enim ad minim veniam quis nostrud.</p>
  </div>
  <div class="btn" style="left:510px;top:485px;width:179px;height:47px">View All Services</div>
</section>

<section class="why">
  <h2 class="abs section-title" style="left:112px;top:2007px;font-size:28px"><span class="accent">WHY</span> NORTHWAY FOUNDATION</h2>
  <p class="abs para" style="left:112px;top:2069px;width:426px">The Northway Foundation was founded from Martin and Helen Greaves’ vision to design an innovative program that would dramatically increase the graduation rates of first-generation college students—those who are first in their family to attend college. For several years prior to starting the foundation, the Greaves endowed scholarships at Ridgeview State University (RSU) and Northfield College (NFC) in order to help students</p>
  <div class="btn" style="left:112px;top:2277px;width:142px;height:50px">Learn More</div>
  <div class="photo" role="img" aria-label="Group of cheerful students outdoors holding books and folders" style="left:600px;top:1976px;width:600px;height:385px;background:linear-gradient(135deg,#c9d88a 0%,#7f9a52 35%,#6f7fa8 65%,#a7a0c4 100%)"></div>
</section>

<section class="blog">
  <h2>LATEST BLOG POST</h2>
  <div class="card" style="left:112px;top:118px;width:478px;height:430px">
    <div role="img" aria-label="Students studying with books in a library" style="height:273px;background:linear-gradient(120deg,#6d4a33 0%,#a36a44 45%,#c9a37c 100%)"></div>
    <span class="date" style="position:absolute;left:43px;top:257px">25 AUG 2021</span>
    <h3 style="position:absolute;left:39px;top:305px;width:420px">Lorem ipsum dolor sit amet, consec tetur adipiscing elitm dolo</h3>
    <p style="position:absolute;left:39px;top:368px;width:420px">Sed ut perspiciatis unde omnis iste natus error sit volup tatem accusantium doloremis iste natus erroque.</p>
  </div>
  <div class="card" style="left:608px;top:118px;width:480px;height:201px">
    <div role="img" aria-label="Two students walking with backpacks" style="position:absolute;left:0;top:0;width:191px;height:201px;background:linear-gradient(135deg,#9fa5a3 0%,#6e7a80 50%,#bfb39b 100%)"></div>
    <span class="date" style="position:absolute;left:212px;top:22px">25 AUG 2021</span>
    <h3 style="position:absolute;left:212px;top:74px;width:260px">Lorem ipsum dolor sit amet, consec tetur adipi</h3>
    <p style="position:absolute;left:212px;top:140px;width:262px">Sed ut perspiciatis unde omnis iste na tus error sit volup tatem.</p>
  </div>
  <div class="card" style="left:608px;top:349px;width:480px;height:199px">
    <div role="img" aria-label="Two children reading books at a desk" style="position:absolute;left:0;top:0;width:191px;height:199px;background:linear-gradient(135deg,#c9b9a4 0%,#8a7563 50%,#4a6e80 100%)"></div>
    <span class="date" style="position:absolute;left:212px;top:20px">25 AUG 2021</span>
    <h3 style="position:absolute;left:212px;top:72px;width:260px">Lorem ipsum dolor sit amet, consec tetur adipi</h3>
    <p style="position:absolute;left:212px;top:138px;width:262px">Sed ut perspiciatis unde omnis iste na tus error sit volup tatem.</p>
  </div>
</section>

<section class="contact">
  <h2 class="abs section-title" style="width:1200px;text-align:center;top:3142px">Contact <span class="accent">Us</span></h2>
  <p class="abs" style="left:200px;width:800px;top:3206px;text-align:center;font-size:14.5px;line-height:25px;color:var(--text)">Sed ut perspiciatis unde omnis iste natus error sit volup tatem accusantium doloremis iste natus erroque.<br>Ade omnis iste natus ecusantium dolora.</p>
  <div class="field" style="left:193px;top:3283px;width:400px;height:50px">First Name</div>
  <div class="field" style="left:606px;top:3283px;width:400px;height:50px">Last Name</div>
  <div class="field" style="left:193px;top:3347px;width:400px;height:50px">Email Address</div>
  <div class="field" style="left:606px;top:3347px;width:400px;height:50px">Phone Number</div>
  <div class="field" style="left:193px;top:3409px;width:813px;height:88px;padding-top:18px">Message</div>
  <div class="btn" style="left:495px;top:3541px;width:210px;height:50px">Send Message
    <svg width="16" height="16" viewBox="0 0 24 24" fill="none" stroke="#fff" stroke-width="2"><path d="M22 2 11 13M22 2l-7 20-4-9-9-4z"/></svg>
  </div>
</section>

<footer class="footer">
  <div class="brand">NORTHWAY FOUNDATION</div>
  <div class="footnav"><span class="accent">HOME</span><span>ABOUT US</span><span>OUR SERVICES</span><span>WHY CHOOSE US</span><span>BLOG</span><span>CONTACT US</span></div>
  <div class="footcontact">
    <svg width="16" height="16" viewBox="0 0 24 24"><path fill="#ee7325" d="M6.6 10.8c1.4 2.8 3.8 5.1 6.6 6.6l2.2-2.2c.3-.3.7-.4 1-.2 1.1.4 2.3.6 3.6.6.6 0 1 .4 1 1V20c0 .6-.4 1-1 1C10.6 21 3 13.4 3 4c0-.6.4-1 1-1h3.5c.6 0 1 .4 1 1 0 1.3.2 2.5.6 3.6.1.3 0 .7-.2 1z"/></svg>
    <span>555-010-2040</span><span style="margin:0 8px">|</span>
    <svg width="18" height="13" viewBox="0 0 22 16"><rect x="1" y="1" width="20" height="14" rx="2" fill="#ee7325"/><path d="M2 2 L11 9 L20 2" stroke="#262626" stroke-width="2" fill="none"/></svg>
    <span>info@northway.org</span>
  </div>
  <div class="btn" style="left:532px;top:188px;width:134px;height:51px">Donate Now</div>
  <div class="rule"></div>
  <div class="copy">© 2021 Company Name. All Rights reserved</div>
</footer>

</body>
</html>
```